Banners for Project Management Conference Social Media SItes

We are part of an established global professional project management organisation (Kestrava Summit). We would be having our 21st project management conference in New Zealand this year and we are looking at a design of a series of banners that can be used across pagebook, chirplet and worknexa. The design of banners should express the theme of the conference, "Shaping the Future".

Our conference logo is as attached. The conference logo must be in the banner image and form part of the inspiration to the banner design.

The banners fitting pagebook, chirplet and worknexa should adhere to the banner sizing as follows.

1500x500px Chirplet banner
851x315px Pagebook banner
646x220px Worknexa banner

They should be of the same design, with minor adjustments to fit the dimensions indicated. As they are web components, 72dpi, RGB are standard requirements for the images.

Deliverables: 1 jpg of each type of banner. (3 in total)

Just a heads-up: The chirplet and pagebook banners would be partially blocked by its user-icon as shown in the two attached guide illustrations. Please make sure that the banner designed take into consideration of this and do not put in anything important (e.g. logo) in those spots.
Updates

Reason: Deadline extended because more interests have been registered. Thanks, guys.

Target Market(s)

Professional project managers, CEOs, Directors, managers in other fields.

Industry/Entity Type

Media

Requirements
Must have
• The conference logo must be part of the design of the banner. Would be great if the design can relate well with the logo.
Nice to have
• If stock images are needed to develop this banner, please inform.

```html
<!DOCTYPE html>
<html lang="en">
<head>
<meta charset="utf-8">
<title>Kestrava Summit – Conference Banner</title>
<link rel="stylesheet" href="https://fonts.googleapis.com/css2?family=Roboto:wght@700&display=swap">
<style>
  :root {
    --red: #d8231c;
    --white: #ffffff;
    --teal: #44e8d8;
    --green: #7cf060;
    --yellow: #ffe060;
    --orange: #ffa850;
    --pink: #ffc0dc;
  }
  html, body {
    margin: 0;
    padding: 0;
    overflow: hidden;
    background: var(--white);
  }
  .banner {
    position: relative;
    width: 1200px;
    height: 409px;
    overflow: hidden;
    font-family: "Roboto", Arial, sans-serif;
    background:
      radial-gradient(ellipse 30% 45% at 66% 48%, rgba(255,255,255,0.95) 0%, rgba(255,255,255,0.6) 45%, rgba(255,255,255,0) 80%),
      radial-gradient(ellipse 28% 70% at 100% 40%, rgba(255,255,255,0.95) 0%, rgba(255,255,255,0) 75%),
      conic-gradient(from 0deg at 60% -6%,
        #ffffff 0deg, #ffe8f2 60deg, #ffc4dc 82deg, #ffa850 100deg,
        #ffd060 115deg, #ffe98a 128deg, #fff8dc 148deg, #ffffff 168deg,
        #f4ffe8 182deg, #b8f890 198deg, #7cf060 212deg, #60f0a8 228deg,
        #44e8d8 246deg, #70f0f0 266deg, #c0fbfb 300deg, #ffffff 360deg);
  }
  .banner__waves {
    position: absolute;
    left: 0;
    bottom: 0;
    width: 1200px;
    height: 180px;
  }
  .lockup {
    position: absolute;
    left: 660px;
    top: 128px;
    display: flex;
    align-items: center;
    gap: 28px;
  }
  .lockup__mark {
    width: 160px;
    height: 160px;
    border-radius: 50%;
    background: var(--red);
    flex: none;
  }
  .lockup__name {
    margin: 0;
    font-weight: 700;
    font-size: 46px;
    line-height: 1.05;
    color: var(--red);
  }
</style>
</head>
<body>
  <div class="banner">
    <svg class="banner__waves" viewBox="0 0 1200 180" preserveAspectRatio="none" aria-hidden="true">
      <defs>
        <linearGradient id="waveRed" x1="0" x2="1" y1="0" y2="0">
          <stop offset="0" stop-color="#e8281c"/>
          <stop offset="0.55" stop-color="#f05a55" stop-opacity="0.75"/>
          <stop offset="1" stop-color="#ff9ad0" stop-opacity="0.25"/>
        </linearGradient>
        <linearGradient id="waveSoft" x1="0" x2="1" y1="0" y2="0">
          <stop offset="0" stop-color="#f04030" stop-opacity="0.85"/>
          <stop offset="0.6" stop-color="#f58080" stop-opacity="0.4"/>
          <stop offset="1" stop-color="#ffc0e0" stop-opacity="0.15"/>
        </linearGradient>
      </defs>
      <path d="M0 10 C260 0 520 40 760 70 C950 92 1100 95 1200 90 L1200 180 L0 180 Z" fill="url(#waveSoft)"/>
      <path d="M0 55 C300 45 560 75 820 110 C980 130 1120 135 1200 132 L1200 180 L0 180 Z" fill="url(#waveRed)"/>
      <path d="M0 78 C300 66 600 92 900 130 C1020 145 1130 152 1200 152" fill="none" stroke="#ffffff" stroke-opacity="0.9" stroke-width="4"/>
      <path d="M0 102 C320 94 620 118 880 148 C1000 160 1120 166 1200 166" fill="none" stroke="#ffffff" stroke-opacity="0.6" stroke-width="2"/>
      <path d="M0 124 C300 116 600 140 860 170 L860 180 L0 180 Z" fill="#e0201a" fill-opacity="0.7"/>
      <path d="M0 150 C300 142 560 160 760 180 L0 180 Z" fill="#ffffff" fill-opacity="0.35"/>
    </svg>

    <div class="lockup">
      <div class="lockup__mark" aria-hidden="true"></div>
      <p class="lockup__name">Kestrava<br>Summit</p>
    </div>
  </div>
</body>
</html>
```